Desk Allies Business Card

Contact Information for Business Card

Janne Voutilainen
Managing Director

3/47 Brindle Street Mitchell ACT 2911

Tel: +61 02 6257 3140
Mob: +61 0427 315 846

Email: janne@deskallies.com.au
Web: www.deskallies.com.au

Colors

Designer to choose colors to be used in the design.

Requirements
Must have
• Logo, Name, Title, Address, Telephone, Mobile, Email Address and Website
• "Desk Ally International Pty Ltd"

```html
<!DOCTYPE html>
<html lang="en">
<head>
<meta charset="utf-8">
<title>Desk Allies Business Card</title>
<link href="https://fonts.googleapis.com/css2?family=Roboto+Condensed:wght@300;400;700&display=swap" rel="stylesheet">
<style>
  :root {
    --backdrop: #e8e6e3;
    --card-white: #ffffff;
    --brand-blue: #3279be;
    --ink-dark: #333333;
    --ink-body: #3a3a3a;
    --rule: #3a3a3a;
    --edge: #5a5a5a;
  }
  * { margin: 0; padding: 0; box-sizing: border-box; }
  html, body {
    width: 1200px; height: 1200px; overflow: hidden;
    background: var(--backdrop);
    font-family: "Roboto Condensed", Arial, sans-serif;
  }
  .canvas { position: relative; width: 1200px; height: 1200px; }

  .card {
    position: absolute; left: 180px; width: 840px; height: 480px;
    border: 1px solid var(--edge);
  }
  .card--front { top: 106px; background: var(--card-white); }
  .card--back { top: 614px; background: var(--brand-blue); }

  .brand { position: absolute; display: flex; align-items: center; }
  .brand__dot { border-radius: 50%; flex: none; }
  .brand__name {
    font-weight: 700; letter-spacing: 0.5px; text-transform: uppercase; line-height: 1;
  }

  .card--front .brand { left: 90px; top: 94px; }
  .card--front .brand__dot { width: 64px; height: 64px; background: var(--brand-blue); margin-right: 20px; }
  .card--front .brand__name { font-size: 38px; color: var(--brand-blue); }

  .card--back .brand { left: 154px; top: 188px; }
  .card--back .brand__dot { width: 92px; height: 92px; background: var(--card-white); margin-right: 28px; }
  .card--back .brand__name { font-size: 50px; color: var(--card-white); }

  .person { position: absolute; right: 50px; top: 224px; text-align: right; }
  .person__name { font-size: 33px; line-height: 1; color: var(--ink-dark); text-transform: uppercase; }
  .person__first { font-weight: 700; }
  .person__last { font-weight: 300; }
  .person__title {
    margin-top: 6px; font-size: 22px; font-weight: 400; letter-spacing: 1.5px;
    color: var(--brand-blue); text-transform: uppercase; line-height: 1;
  }
  .accent-tab { position: absolute; left: 820px; top: 226px; width: 20px; height: 54px; background: var(--brand-blue); }

  .divider { position: absolute; left: 274px; top: 299px; width: 516px; height: 1px; background: var(--rule); }

  .contact { position: absolute; left: 90px; font-size: 20px; color: var(--ink-body); line-height: 1; letter-spacing: 0.3px; }
  .contact__label { color: var(--brand-blue); font-weight: 700; margin-right: 4px; }
  .contact--tel { top: 289px; }
  .contact--mob { top: 316px; }
  .contact--email { top: 368px; }
  .contact--web { top: 395px; }

  .address {
    position: absolute; right: 50px; top: 316px; text-align: right;
    font-size: 20px; color: var(--ink-body); line-height: 27px; letter-spacing: 0.3px;
  }
</style>
</head>
<body>
<main class="canvas">
  <section class="card card--front" aria-label="Business card front">
    <div class="brand">
      <span class="brand__dot"></span>
      <span class="brand__name">Desk Allies</span>
    </div>

    <div class="person">
      <div class="person__name"><span class="person__first">Janne</span> <span class="person__last">Voutilainen</span></div>
      <div class="person__title">Managing Director</div>
    </div>
    <span class="accent-tab"></span>

    <span class="divider"></span>

    <div class="contact contact--tel"><span class="contact__label">t:</span>+61 02 6257 3140</div>
    <div class="contact contact--mob"><span class="contact__label">m:</span>+61 0427 315 846</div>
    <div class="contact contact--email"><span class="contact__label">e:</span>janne@deskallies.com.au</div>
    <div class="contact contact--web"><span class="contact__label">w:</span>www.deskallies.com.au</div>

    <address class="address" style="font-style: normal;">
      3/47 Brindle Street<br>
      Mitchell ACT 2911
    </address>
  </section>

  <section class="card card--back" aria-label="Business card back">
    <div class="brand">
      <span class="brand__dot"></span>
      <span class="brand__name">Desk Allies</span>
    </div>
  </section>
</main>
</body>
</html>
```